Flat bootstrap design for existing site

I'm looking for a modern flat design based around an existing logo. This has to be a custom design (no external templates), and implemented into a bootstrap framework.

The logo is attached as 2 versions - choose whichever you want, that flows better with whatever design you choose.

Added screenshots of the existing site (currently using the default bootstrap layouts). Please make your designs around those pages in the screenshots (i.e. the homepage only has the postal code input and the header). The active page has 3 screenshots, because I wanted to illustrate the other states that would be visible (in the table rows).

This is a moving/junk removal website, just for some context.

Here's some example websites (flat designs) that I like, just to give you an idea of what I'm after.

https://www.plivento.com/
https://hoskadel.com/
https://trumvex.com/
https://bravolinth.com/en/

• It must be a modern/simple flat design, that is built around the existing logo (attached).
• It has to be implemented using bootstrap.

```html
<!DOCTYPE html>
<html lang="en">
<head>
<meta charset="utf-8">
<title>Haulro — Become a Driver</title>
<link href="https://fonts.googleapis.com/css2?family=Lato:wght@400;700&display=swap" rel="stylesheet">
<style>
:root{
  --sky:#38ccfd;
  --sky-light:#52d3fc;
  --page:#f4f4f4;
  --white:#ffffff;
  --ink:#555a5e;
  --placeholder:#b9bcbf;
  --orange:#f26522;
}
*{box-sizing:border-box;margin:0;padding:0}
html,body{width:1200px;height:667px;overflow:hidden}
body{background:var(--page);font-family:"Lato",Arial,sans-serif;position:relative}
.site-header{position:absolute;left:0;top:0;width:1200px;height:89px;background:var(--sky)}
.brand{position:absolute;left:79px;top:0;width:177px;height:89px;background:var(--sky-light);
  display:flex;align-items:center;justify-content:center;gap:10px;color:var(--white);
  font-weight:700;font-size:28px;letter-spacing:1px}
.brand-dot{width:14px;height:14px;border-radius:50%;background:var(--white)}
.main-nav a{position:absolute;top:38px;color:var(--white);font-weight:700;font-size:16px;text-decoration:none;line-height:18px}
.main-nav .active{left:600px;top:31px;width:68px;height:31px;border:2px solid var(--white);
  display:flex;align-items:center;justify-content:center}
.cursor{position:absolute;left:658px;top:50px}
.card{position:absolute;left:133px;width:401px;background:var(--sky)}
.intro{top:133px;height:177px}
.intro::after{content:"";position:absolute;right:-23px;top:77px;border-left:23px solid var(--sky);
  border-top:13px solid transparent;border-bottom:13px solid transparent}
.intro h2{position:absolute;left:18px;top:18px;color:var(--white);font-size:19px;font-weight:700;letter-spacing:.2px}
.intro p{position:absolute;left:113px;top:52px;color:var(--ink);font-size:18px;line-height:29px}
.intro p span{display:block}
.intro p span+span{padding-left:2px}
.radius{top:349px;height:135px}
.radius label{position:absolute;left:56px;top:22px;color:var(--white);font-size:16px;font-weight:700;line-height:21px}
.field{background:var(--white);border:none;font-family:inherit;color:var(--placeholder);font-size:14px;padding-left:22px;display:flex;align-items:center}
.radius .field{position:absolute;left:58px;top:83px;width:116px;height:27px;padding-left:11px}
.apply-form{position:absolute;left:611px;top:132px;width:510px;height:497px;background:var(--sky)}
.row{position:absolute;left:0;width:510px;height:34px}
.row label{position:absolute;right:358px;top:6px;color:var(--white);font-weight:700;font-size:17px;white-space:nowrap}
.row .field{position:absolute;left:190px;top:0;width:311px;height:34px}
.apply{position:absolute;left:190px;top:436px;width:112px;height:33px;background:var(--orange);color:var(--white);
  font-weight:700;font-size:17px;display:flex;align-items:center;justify-content:center}
</style>
</head>
<body>
<header class="site-header">
  <div class="brand"><span class="brand-dot"></span>HAULRO</div>
  <nav class="main-nav">
    <a class="active" href="#">BOOK</a>
    <a href="#" style="left:690px">HOW IT WORKS</a>
    <a href="#" style="left:843px">BECOME A DRIVER</a>
    <a href="#" style="left:1012px">LOGIN</a>
  </nav>
  <svg class="cursor" width="24" height="30" viewBox="0 0 24 30"><path d="M2 2 L2 24 L8 18 L12 27 L15 26 L11 17 L20 17 Z" fill="#fff" stroke="#38ccfd" stroke-width="1.5"/></svg>
</header>

<section class="card intro">
  <h2>INTERESTED IN BECOMING A DRIVER?</h2>
  <p><span>Complete this form,</span><span>and we’ll assess it</span><span>and get back to you.</span></p>
</section>

<section class="card radius">
  <label>How many km away from your home<br>do you want to service?</label>
  <div class="field">Kilometer</div>
</section>

<form class="apply-form">
  <div class="row" style="top:28px"><label>First Name</label><div class="field">First Name</div></div>
  <div class="row" style="top:69px"><label>Last Name</label><div class="field">Last Name</div></div>
  <div class="row" style="top:112px"><label>Email</label><div class="field">Email</div></div>
  <div class="row" style="top:155px"><label>Password</label><div class="field">Password</div></div>
  <div class="row" style="top:198px"><label>Phone</label><div class="field">Phone</div></div>
  <div class="row" style="top:242px"><label>Address</label><div class="field">Address</div></div>
  <div class="row" style="top:287px"><label>City</label><div class="field">City</div></div>
  <div class="row" style="top:332px"><label>Province</label><div class="field">Province</div></div>
  <div class="row" style="top:379px"><label>Postal Code</label><div class="field">Postal Code</div></div>
  <div class="apply">APPLY</div>
</form>
</body>
</html>
```